Corvane Electrical Solutions

On one side. LOGO (underneath:) Commercial Industrial Residential

- NAME & CONTACT DETAILS

Marcus T. Hollings
Project Manager

(Cell icon) (441) 582-6197
(Email icon) cvnelectricalsoultions@mailventra.com
(Facebook & Instagram icons )@cvnelectricalsolutions

Other side: LOGO - underneath ELECTRICAL CONSTRUCTION & MAINTENANCE . LED LIGHTING & AUTOMATION . LIFE SAFETY SYSTEMS (FIRE ALARM / SECURITY) . DATA & COMMUNICATION

```html
<!DOCTYPE html>
<html lang="en">
<head>
<meta charset="utf-8">
<title>Corvane Electrical Solutions – Business Card</title>
<link rel="stylesheet" href="https://fonts.googleapis.com/css2?family=Montserrat:wght@500&family=Arimo:wght@400;700&display=swap">
<style>
  :root {
    --backdrop: #2a2a2c;
    --teal: #176179;
    --teal-deep: #0f4d62;
    --paper: #fbfbfb;
    --ink: #3b3b3b;
    --white: #ffffff;
  }
  * { box-sizing: border-box; margin: 0; padding: 0; }
  html, body {
    width: 1200px; height: 997px; overflow: hidden;
    background: var(--backdrop);
  }
  .stage {
    position: relative; width: 1200px; height: 997px;
    display: flex; align-items: center; justify-content: center; gap: 40px;
  }
  .card {
    position: relative; width: 540px; height: 309px;
    box-shadow: 0 12px 30px rgba(0,0,0,.45);
  }
  .card--front {
    background: linear-gradient(135deg, var(--teal) 0%, var(--teal-deep) 100%);
    color: var(--white);
  }
  .card--back { background: var(--paper); color: var(--ink); }

  .brand {
    display: flex; align-items: center; gap: 12px;
    font-family: "Montserrat", sans-serif; font-weight: 500;
    text-transform: uppercase; letter-spacing: 2px; line-height: 1.15;
  }
  .brand__mark { width: 14px; height: 14px; flex: none; }
  .card--front .brand {
    position: absolute; left: 56px; top: 78px; font-size: 24px; color: var(--white);
  }
  .card--front .brand__mark { background: var(--white); }
  .card--back .brand {
    position: absolute; right: 36px; top: 40px; font-size: 17px; color: var(--teal);
  }
  .card--back .brand__mark { background: var(--teal); }

  .services {
    position: absolute; left: 56px; right: 30px; bottom: 54px;
    font-family: "Arimo", sans-serif; font-size: 11.5px; letter-spacing: 1px;
    line-height: 1.7; text-transform: uppercase; color: rgba(255,255,255,.92);
  }

  .person {
    position: absolute; left: 34px; bottom: 30px;
    font-family: "Arimo", sans-serif;
  }
  .person__name {
    font-weight: 700; font-size: 17px; color: var(--teal);
    text-transform: uppercase; letter-spacing: .5px;
  }
  .person__role { font-size: 14px; color: var(--ink); margin-bottom: 10px; }
  .contacts { list-style: none; font-size: 11.5px; color: var(--ink); }
  .contacts li { display: flex; align-items: center; gap: 6px; height: 19px; }
  .contacts svg { width: 13px; height: 13px; flex: none; }

  .tagline {
    position: absolute; right: 36px; bottom: 78px;
    font-family: "Arimo", sans-serif; font-size: 13px; color: var(--teal);
  }
</style>
</head>
<body>
<main class="stage">
  <section class="card card--front" aria-label="Card front">
    <div class="brand"><span class="brand__mark"></span><span>Corvane<br>Electrical<br>Solutions</span></div>
    <p class="services">
      Electrical Construction &amp; Maintenance . LED Lighting &amp; Automation .<br>
      Life Safety Systems (Fire Alarm / Security) . Data &amp; Communication
    </p>
  </section>

  <section class="card card--back" aria-label="Card back">
    <div class="brand"><span class="brand__mark"></span><span>Corvane<br>Electrical<br>Solutions</span></div>
    <p class="tagline">Commercial Industrial Residential</p>
    <div class="person">
      <h1 class="person__name">Marcus T. Hollings</h1>
      <p class="person__role">Project Manager</p>
      <ul class="contacts">
        <li>
          <svg viewBox="0 0 16 16" aria-hidden="true"><circle cx="8" cy="8" r="8" fill="#176179"/><path d="M5.2 4.2l1.6-.2.8 2-1 .8c.5 1.1 1.3 1.9 2.4 2.4l.8-1 2 .8-.2 1.6c-3.6.2-6.6-2.8-6.4-6.4z" fill="#fff"/></svg>
          (441) 582-6197
        </li>
        <li>
          <svg viewBox="0 0 16 16" aria-hidden="true"><circle cx="8" cy="8" r="8" fill="#176179"/><rect x="4" y="5.2" width="8" height="5.6" fill="none" stroke="#fff" stroke-width="1"/><path d="M4 5.4l4 3 4-3" fill="none" stroke="#fff" stroke-width="1"/></svg>
          cvnelectricalsoultions@mailventra.com
        </li>
        <li>
          <svg viewBox="0 0 16 16" aria-hidden="true"><circle cx="8" cy="8" r="8" fill="#176179"/></svg>
          @cvnelectricalsolutions
        </li>
        <li>
          <svg viewBox="0 0 16 16" aria-hidden="true"><circle cx="8" cy="8" r="8" fill="#176179"/></svg>
          @cvnelectricalsolutions
        </li>
      </ul>
    </div>
  </section>
</main>
</body>
</html>
```